I would like an amazing design for a eCommerce website called trekharbor.net.

The logo was designed on PixelGuild and is attached below. Whatever your design - it MUST use this logo. Please don't waste your time designing new logos.

The logo is on both black and white backgrounds as I've not yet made my mind up whether to ditch "cool black" in favour of more "fresh, clean white"! I'd like to look at both options.

Trek Harbor is going to be the first destination of choice for anyone who is bored or frustrated at home and wants a life full of adventure. It will stock outdoor clothing and equipment, training kit, expedition gear, and travel clothing and accessories.

But it is a very cool place to go. A fun and exciting Aladdin's cave full of fantastic adventure kit. We will stock inflatable pack rafts, machetes, hammocks and other expedition gear as well as standard outdoor clothing.

This is NOT a geeky outdoor store selling pac-a-macs and walking poles.

The unique thing is that everything stocked is hand selected by me, Tom Weller, an experienced explorer who became the first person to walk the Amazon in 2010. tomweller.net is my site. I now make TV for Horizon Vision.

There will be items at every price level from "only the best" - absolute top end kit, to "get the job done" - stuff that won't break the bank. Everything stocked works. If it doesn't - I won't sell it.

So although the theme is fun and adventurous I have to have it also feeling like a place of professional, expert advice. A place of substance and depth.

Thanks in advance for all your ideas and designs!

Best
Tom

The designs that I like the best have used jungle images as background wallpaper - possible with a green tint to them so that they really do look like background rather than the focus. The focus should obviously be the kit for sale. The best designs have this on a fresh white or light grey background so that it stands out. I like the main logo being in a black header and footer. But the feel of the site can easily become too dark if too much back is used or if the green background image is too dark. We want adventure and cool - but it has to feel light and professional enough to be accessible by people of all ages. Most websites that are successful are white after all and whilst I'd like to be a bit more adventurous than that we shouldn't over do the darkness!

I'm not really a massive fan of side bars and would hope that whichever site I chose had a mega menu system like Marlow Finch that could navigate quickly and easily to any item intuitively.

Any sliders must be about selling kit not images of me.

Thanks so much to everyone who has submitted designs - there are some VERY cool ones out there at the moment

Best,
Tom

Target Market(s)

The target market is primarily 16 to 50 years old outdoor enthusiasts however I will be selling to older people and kids, male and female, so it can't be too modern, too macho, or too complicated to put anyone off.

Requirements
Must have
• Bold, professional, adventurous feel. Not cluttered but not so minimalist that it looks boring too. I would like to select a few colours and work with them.
• Red for high lighted emphasis. See logo
• Greens/blacks/greys as background.
• Clean menu system. I'm probably going use a tailored version of http://bright-bright.shopbuilder.net with mega menus.
Nice to have
• Some personalisation that makes the site mine. Use of hi res images below as background could work although I am keen for the site to look clean and easy to navigate.
Should not have
• Hundreds of boxes and text and clutter. I want this site to show off the items in a classy manner. This is NOT games depot.com! This is a site where hand selected items are proudly displayed and put together, after a lot of thought.

```html
<!DOCTYPE html>
<html lang="en">
<head>
<meta charset="utf-8">
<title>Trek Harbor – Everything for a life of adventure</title>
<link rel="stylesheet" href="https://fonts.googleapis.com/css2?family=Arimo:wght@400;700&family=Oswald:wght@500;600&family=Russo+One&display=swap">
<style>
:root{
  --red:#e3161e;
  --black:#0b0b0b;
  --header:#1c1c1d;
  --nav:#0e0e0e;
  --white:#ffffff;
  --text-dark:#222222;
  --link-blue:#2a9fe0;
  --green:#17a54a;
  --social-blue:#3b5b98;
}
*{box-sizing:border-box;margin:0;padding:0}
html,body{width:700px;height:1200px;overflow:hidden;background:var(--black)}
body{position:relative;font-family:"Arimo",Arial,sans-serif;color:var(--white)}
.abs{position:absolute}

/* header */
.site-header{left:0;top:0;width:700px;height:55px;background:var(--header);border-top:2px solid var(--red)}
.brand{left:77px;top:11px}
.brand-name{font-family:"Oswald",sans-serif;font-weight:600;font-size:21px;line-height:21px;color:var(--red);letter-spacing:1px;text-transform:uppercase}
.brand-tagline{font-size:8.5px;color:var(--white);margin-top:2px}
.utility-links{right:77px;top:6px;display:flex;gap:10px;font-size:6.5px;color:#ddd}
.utility-links span{display:flex;align-items:center;gap:3px}
.contact{right:77px;top:25px;font-size:8px;line-height:14px}
.contact div{display:flex;align-items:center;gap:5px}

/* nav */
.main-nav{left:0;top:55px;width:700px;height:23px;background:var(--nav);border-top:1px solid #2a2a2a}
.nav-list{left:77px;top:0;display:flex;list-style:none;height:22px}
.nav-list li{font-size:8.5px;line-height:22px;padding:0 13px;border-right:1px solid #2c2c2c}
.nav-list li.active{background:var(--red);padding:0 14px}
.search{left:509px;top:4px;width:114px;height:14px;display:flex}
.search-field{flex:1;background:#4a4a4a;border:1px solid #5a5a5a}
.search-btn{width:15px;background:var(--red);display:flex;align-items:center;justify-content:center}

/* hero */
.hero{left:0;top:78px;width:700px;height:298px;
  background:linear-gradient(180deg,#4f5a2a 0%,#6d7236 18%,#3c4220 36%,#585032 52%,#7a6a44 64%,#4a3e26 78%,#2e2816 100%)}
.hero-arrow{top:122px;width:28px;height:42px;background:var(--red);display:flex;align-items:center;justify-content:center}
.hero-arrow.prev{left:0}
.hero-arrow.next{right:0}
.hero-caption{left:61px;top:172px}
.tag-red{display:inline-block;background:var(--red);font-family:"Oswald",sans-serif;font-weight:600;color:var(--white);text-transform:uppercase;line-height:1}
.tag-white{display:inline-block;background:var(--white);color:var(--red);font-family:"Oswald",sans-serif;font-weight:500;line-height:1}
.hero-caption .tag-red{font-size:23px;padding:4px 8px}
.hero-caption .tag-white{font-size:12.5px;padding:2px 5px;margin:3px 0 0 20px}
.read-more{display:inline-block;margin:5px 0 0 130px;background:var(--black);color:var(--white);font-family:"Oswald",sans-serif;font-size:10px;padding:3px 6px;border-right:3px solid var(--red)}
.hero-dots{left:331px;top:357px;display:flex;gap:3px}
.hero-dots i{width:7px;height:7px;border-radius:50%;background:var(--black)}
.hero-dots i.on{background:var(--red)}
.hero-rule{left:0;top:376px;width:700px;height:4px;background:#111}

/* featured */
.featured{left:0;top:380px;width:700px;height:325px;background:radial-gradient(ellipse at 50% 40%,#575757 0%,#444 60%,#363636 100%)}
.section-title{left:0;top:26px;width:700px;text-align:center;font-family:"Russo One",sans-serif;font-weight:400;font-size:26px;color:#f0f0f0}
.product{top:71px;width:172px;height:229px;border:1px solid #222;background:#1b1b1b}
.product-img{left:0;top:0;width:170px;height:205px}
.price-badge{right:14px;top:56px;width:46px;height:46px;border-radius:50%;background:var(--red);text-align:center;font-family:"Russo One",sans-serif}
.price-badge s{display:block;font-size:8px;margin-top:9px}
.price-badge b{display:block;font-size:14px;font-weight:400}
.product-caption{left:15px;top:156px}
.product-caption .tag-red{font-size:16px;padding:2px 5px}
.product-caption .tag-white{font-size:9.5px;padding:1px 4px;margin:2px 0 0 18px}
.product-bar{left:0;top:205px;width:170px;height:22px;display:flex}
.stars{width:73px;background:#151515;display:flex;align-items:center;justify-content:center}
.add-cart{flex:1;background:var(--red);display:flex;align-items:center;justify-content:center;gap:4px;font-family:"Russo One",sans-serif;font-size:8.5px}

/* story */
.story{left:0;top:705px;width:700px;height:193px;background:linear-gradient(90deg,#ededed 0%,#ffffff 35%,#f6f6f6 60%,#e6e6e6 100%)}
.story-photo{left:420px;top:20px;width:280px;height:173px;
  background:linear-gradient(100deg,#f2f2f2 0%,#c9c9c9 18%,#7c7c7c 38%,#9d9d9d 55%,#5e5e5e 75%,#bdbdbd 100%)}
.story-copy{left:77px;top:28px;width:350px}
.story-copy .tag-red{font-size:22px;padding:4px 6px}
.story-sub{display:inline-block;background:var(--black);color:var(--white);font-family:"Oswald",sans-serif;font-weight:500;font-size:13px;letter-spacing:.35px;padding:3px 6px;margin-top:3px}
.story-copy p{color:var(--text-dark);font-size:10px;line-height:12.5px;margin:10px 0 0 7px;width:318px}

/* tweet */
.tweet-band{left:0;top:898px;width:700px;height:57px;background:linear-gradient(#2a2727,#1a1818);border-bottom:1px solid #333;text-align:center}
.tweet-handle{left:0;top:16px;width:700px;font-size:8px;color:var(--link-blue)}
.tweet-text{left:120px;top:29px;width:460px;font-size:7.5px;color:#999;display:flex;align-items:center;gap:7px}
.tweet-text a{color:var(--red);text-decoration:none}
.tweet-time{left:0;top:42px;width:700px;font-size:5px;color:#666}

/* footer */
.site-footer{left:0;top:955px;width:700px;height:220px;background:var(--black)}
.footer-title{font-size:11px;font-weight:400;color:var(--red)}
.posts{left:77px;top:24px;width:240px}
.post{padding:6px 0 7px;border-bottom:1px dashed #333;font-size:6.5px;line-height:9px;color:#888}
.post:last-child{border-bottom:none}
.post h4{font-size:7px;font-weight:400;color:#ddd;margin-bottom:1px}
.post a{color:var(--link-blue);display:block;margin-top:2px}
.useful{left:362px;top:24px}
.useful ul{list-style:none;margin-top:5px}
.useful li{font-size:6px;line-height:12.5px;color:#999}
.useful li::before{content:"•";margin-right:4px;color:#ccc}
.newsletter{left:462px;top:27px;width:161px;height:75px;background:#1c1c1c;border:1px solid #333;padding:7px 5px}
.newsletter p{font-size:5.5px;color:#ccc;margin:5px 0 6px}
.email-field{height:14px;background:#3a3a3a;border:1px solid #555;font-size:5.5px;line-height:12px;padding-left:4px;color:#ddd}
.subscribe{margin:5px 0 0 105px;width:48px;height:13px;background:var(--green);font-size:6.5px;line-height:13px;text-align:center;border-radius:2px}
.stay{left:462px;top:123px;width:161px;height:15px;display:flex;gap:1px}
.stay-label{width:84px;background:#3a3a3a;font-size:7.5px;line-height:15px;text-align:center;color:#ddd}
.stay-icon{width:15px;background:#2b2b2b;border:1px solid #444;display:flex;align-items:center;justify-content:center}
.stay-icon::after{content:"";width:5px;height:5px;border-radius:50%;background:#cfcfcf}
.stay-icon.primary{background:var(--social-blue);border-color:var(--social-blue)}
.stay-icon.primary::after{background:#fff}
.footer-brand{left:464px;top:160px}
.footer-brand .brand-name{font-size:17px;line-height:17px}
.footer-brand .brand-tagline{font-size:7px}

.bottom-bar{left:0;top:1175px;width:700px;height:25px;background:#141414}
.copyright{left:77px;top:9px;font-size:6px;color:#666}
.payments{right:77px;top:6px;display:flex;gap:3px}
.payments i{width:21px;height:13px;border-radius:2px;background:#f4f4f4;border:1px solid #bbb}
.payments i.dark{background:#3c4250;border-color:#5a6070}
.payments i.red{background:#2a2a2a;border-color:#555}
</style>
</head>
<body>

<header class="abs site-header">
  <div class="abs brand">
    <div class="brand-name">Trek Harbor</div>
    <div class="brand-tagline">Everything for a life of adventure - by Tom Weller</div>
  </div>
  <div class="abs utility-links">
    <span><svg width="8" height="7" viewBox="0 0 8 7"><path d="M0 1h1.5l1 4h4l1-3H2" fill="none" stroke="#fff" stroke-width="0.9"/><circle cx="3" cy="6.3" r=".6" fill="#fff"/><circle cx="6" cy="6.3" r=".6" fill="#fff"/></svg>View Cart</span>
    <span><svg width="7" height="7" viewBox="0 0 7 7"><circle cx="3.5" cy="2" r="1.8" fill="#fff"/><path d="M0 7c0-2.5 1.5-3.5 3.5-3.5S7 4.5 7 7z" fill="#fff"/></svg>My Account</span>
    <span><svg width="4" height="7" viewBox="0 0 4 7"><circle cx="2.5" cy="1" r="1" fill="#fff"/><path d="M1 3h2.2L2.4 7H1.2z" fill="#fff"/></svg>Customer Service</span>
  </div>
  <div class="abs contact">
    <div><svg width="8" height="8" viewBox="0 0 8 8"><path d="M1.5 0.5l1.5 1.8-1 1a5 5 0 0 0 2.7 2.7l1-1L7.5 6.5 6.5 7.6C3.5 7.4 0.6 4.5 0.4 1.5z" fill="#fff"/></svg>0000-0000000000</div>
    <div><svg width="9" height="7" viewBox="0 0 9 7"><rect x=".5" y=".5" width="8" height="6" fill="#fff"/><path d="M.5.5l4 3.2 4-3.2" fill="none" stroke="#1c1c1d" stroke-width=".8"/></svg>info@trekharbor.net</div>
  </div>
</header>

<nav class="abs main-nav">
  <ul class="abs nav-list">
    <li class="active">Home</li>
    <li>About Us</li>
    <li>Our Products</li>
    <li>Latest Arrivals</li>
    <li>FAQ</li>
    <li>Contact Us</li>
  </ul>
  <div class="abs search">
    <div class="search-field"></div>
    <div class="search-btn"><svg width="8" height="8" viewBox="0 0 8 8"><circle cx="3.2" cy="3.2" r="2.3" fill="none" stroke="#fff" stroke-width="1.1"/><path d="M5 5l2.5 2.5" stroke="#fff" stroke-width="1.3"/></svg></div>
  </div>
</nav>

<section class="abs hero" role="img" aria-label="Explorer wading chest-deep through a flooded jungle with a large backpack">
  <div class="abs hero-arrow prev"><svg width="10" height="22" viewBox="0 0 10 22"><path d="M9 1L1 11l8 10" fill="none" stroke="#fff" stroke-width="1.4"/></svg></div>
  <div class="abs hero-arrow next"><svg width="10" height="22" viewBox="0 0 10 22"><path d="M1 1l8 10-8 10" fill="none" stroke="#fff" stroke-width="1.4"/></svg></div>
</section>
<div class="abs hero-caption">
  <div class="tag-red">Lorem Ipsum</div><br>
  <div class="tag-white">Lorem ipsum dolor sit amet.</div><br>
  <div class="read-more">Read More</div>
</div>
<div class="abs hero-dots"><i class="on"></i><i></i><i></i><i></i></div>
<div class="abs hero-rule"></div>

<svg width="0" height="0" style="position:absolute"><defs><path id="st" d="M5 0l1.5 3.2 3.5.4-2.6 2.4.7 3.5L5 7.8 1.9 9.5l.7-3.5L0 3.6l3.5-.4z"/></defs></svg>

<section class="abs featured">
  <h2 class="abs section-title">Featured Items</h2>

  <article class="abs product" style="left:77px">
    <div class="abs product-img" role="img" aria-label="Explorer with a blue backpack wading a jungle river" style="background:linear-gradient(180deg,#5e6e3a 0%,#3f5230 30%,#6b6a48 55%,#8a6e46 75%,#4c4530 100%)"></div>
    <div class="abs price-badge"><s>£299</s><b>£199</b></div>
    <div class="abs product-caption"><div class="tag-red">Lorem Ipsum</div><br><div class="tag-white">Lorem ipsum dolor sit amet.</div></div>
    <div class="abs product-bar">
      <div class="stars"><svg width="66" height="10" viewBox="0 0 66 10"><g fill="#e3161e"><use href="#st"/><use href="#st" x="14"/><use href="#st" x="28"/><use href="#st" x="42"/></g><use href="#st" x="56" fill="#777"/></svg></div>
      <div class="add-cart"><svg width="10" height="8" viewBox="0 0 10 8"><path d="M0 1h2l1 5h5l1.3-4H2.5" fill="none" stroke="#fff" stroke-width="1"/><circle cx="3.8" cy="7.3" r=".7" fill="#fff"/><circle cx="7.5" cy="7.3" r=".7" fill="#fff"/></svg>ADD TO CART</div>
    </div>
  </article>

  <article class="abs product" style="left:265px">
    <div class="abs product-img" role="img" aria-label="Explorer in a cap carrying a red backpack through green forest" style="background:linear-gradient(180deg,#3e7a2c 0%,#2d5a20 35%,#4f6a34 60%,#2f4a22 80%,#3d6a2a 100%)"></div>
    <div class="abs price-badge"><s>£199</s><b>£99</b></div>
    <div class="abs product-caption"><div class="tag-red">Lorem Ipsum</div><br><div class="tag-white">Lorem ipsum dolor sit amet.</div></div>
    <div class="abs product-bar">
      <div class="stars"><svg width="66" height="10" viewBox="0 0 66 10"><g fill="#e3161e"><use href="#st"/><use href="#st" x="14"/><use href="#st" x="28"/></g><g fill="#777"><use href="#st" x="42"/><use href="#st" x="56"/></g></svg></div>
      <div class="add-cart"><svg width="10" height="8" viewBox="0 0 10 8"><path d="M0 1h2l1 5h5l1.3-4H2.5" fill="none" stroke="#fff" stroke-width="1"/><circle cx="3.8" cy="7.3" r=".7" fill="#fff"/><circle cx="7.5" cy="7.3" r=".7" fill="#fff"/></svg>ADD TO CART</div>
    </div>
  </article>

  <article class="abs product" style="left:452px">
    <div class="abs product-img" role="img" aria-label="Explorer with a blue backpack crossing a rocky jungle stream" style="background:linear-gradient(180deg,#5a5a46 0%,#3e5a34 30%,#6e7e5e 55%,#8a8e7a 75%,#44503a 100%)"></div>
    <div class="abs price-badge"><s>£399</s><b>£299</b></div>
    <div class="abs product-caption"><div class="tag-red">Lorem Ipsum</div><br><div class="tag-white">Lorem ipsum dolor sit amet.</div></div>
    <div class="abs product-bar">
      <div class="stars"><svg width="66" height="10" viewBox="0 0 66 10"><g fill="#e3161e"><use href="#st"/><use href="#st" x="14"/><use href="#st" x="28"/><use href="#st" x="42"/></g><use href="#st" x="56" fill="#777"/></svg></div>
      <div class="add-cart"><svg width="10" height="8" viewBox="0 0 10 8"><path d="M0 1h2l1 5h5l1.3-4H2.5" fill="none" stroke="#fff" stroke-width="1"/><circle cx="3.8" cy="7.3" r=".7" fill="#fff"/><circle cx="7.5" cy="7.3" r=".7" fill="#fff"/></svg>ADD TO CART</div>
    </div>
  </article>
</section>

<section class="abs story">
  <div class="abs story-photo" role="img" aria-label="Black and white portrait of a laughing explorer with a hand on his head"></div>
  <div class="abs story-copy">
    <div class="tag-red">Lorem Ipsum Dolor</div><br>
    <div class="story-sub">Nulla lobortis consequat mauris, eget eleifend nunc viverra</div>
    <p>Nulla lobortis consequat mauris, eget eleifend nunc viverra viverra. Ut ac risus odio. Aliquam pretium purus sed nulla feugiat blandit. Cras vel libero ut lacus eleifend tempor. Phasellus eleifend, magna non tincidunt accumsan, justo arcu cursus ipsum, non porttitor sapien quam vel magna. Maecenas elit nisl, molestie nec dapibus nec, aliquet a erat. Donec scelerisque lacus a libero suscipit auctor volutpat enim euismod. Mauris porta, lacus ut ullamcorper sodales.</p>
  </div>
</section>

<section class="abs tweet-band">
  <div class="abs tweet-handle">@Loremipsum</div>
  <div class="abs tweet-text"><svg width="14" height="14" viewBox="0 0 14 14"><circle cx="7" cy="7" r="6" fill="#2a9fe0"/></svg><span>dolor sit amet, consectetur adipiscing elit. Nulla lobortis consequat mauris, eget eleifend nunc viverra viverra. <a>http://Ut.ac/risus.com</a></span></div>
  <div class="abs tweet-time">about 25 hours, 10 minutes ago</div>
</section>

<footer class="abs site-footer">
  <div class="abs posts">
    <h3 class="footer-title">Latest Posts</h3>
    <div class="post"><h4>Lorem ipsum dolor</h4>Consectetur - Nulla lobortis consequat mauris, eget eleifend nunc viverra viverra.<a>read more</a></div>
    <div class="post"><h4>Integer eget ligula lectus</h4>Integer - Lorem ipsum dolor sit amet, consectetur adipiscing elit. Nulla lobortis consequat mauris, eget eleifend nunc viverra viverra. Ut ac risus odio. Aliquam pretium purus sed nulla feugiat blandit. Cras vel libero ut lacus eleifend tempor. Phasellus eleifend, magna non tincidunt accumsan, justo arcu cursus ipsum, non porttitor sapien.<a>read more</a></div>
    <div class="post"><h4>Donec at nisl augue</h4>Cras viverra - Donec a lectus non purus ultricies eleifend. Duis nec augue eget lorem vestibulum suscipit. Integer eget ligula lectus, eget pulvinar diam.<a>read more</a></div>
  </div>
  <div class="abs useful">
    <h3 class="footer-title">Useful Links</h3>
    <ul>
      <li>Lorem ipsum dolor sit</li><li>Amet, consectetur</li><li>Adipiscing elit. Nulla</li><li>Lobortis consequat</li><li>Mauris, eget eleifend</li><li>Nunc viverra viverra.</li><li>Ut ac risus odio.</li><li>Aliquam pretium</li><li>Purus sed nulla</li><li>Feugiat blandit. Cras</li><li>Vel libero ut lacus</li><li>Eleifend tempor.</li>
    </ul>
  </div>
  <div class="abs newsletter">
    <h3 class="footer-title">NEWSLETTER</h3>
    <p>Sign up to our newsletter for the latest news and special offers.</p>
    <div class="email-field">Enter your email here</div>
    <div class="subscribe">Subscribe</div>
  </div>
  <div class="abs stay">
    <div class="stay-label">STAY IN TOUCH</div>
    <i class="stay-icon primary"></i><i class="stay-icon"></i><i class="stay-icon"></i><i class="stay-icon"></i><i class="stay-icon"></i>
  </div>
  <div class="abs brand footer-brand">
    <div class="brand-name">Trek Harbor</div>
    <div class="brand-tagline">Everything for a life of adventure - by Tom Weller</div>
  </div>
</footer>

<div class="abs bottom-bar">
  <div class="abs copyright">Copyright © 2014 trekharbor.net. All Rights Reserved.</div>
  <div class="abs payments"><i></i><i></i><i></i><i class="dark"></i><i class="red"></i></div>
</div>

</body>
</html>
```